Coffeeshop menu for filter tip

We want to have a cannabis (coffeeshop) menu in the size 25mm wide x 60mm wide. Some examples attached.

it must have the following text:
Menu

WEED p/g
Vortigan €16
Tangerosa €14
Dusk Rover €14
Mangolina €16
Ultra Fern €14
Amber Hermit €14

HASH p/g
Nepali Bronze €12
Velvet Ember€11
Cedar Pine €14
Red Fable €10

Target Market(s)

tourist in Amsterdam

Requirements
Nice to have
• cannabis sign leaf
• No Cigarettes allowed symbol

```html
<!DOCTYPE html>
<html lang="en">
<head>
<meta charset="utf-8">
<title>Coffeeshop Menu</title>
<link href="https://fonts.googleapis.com/css2?family=Germania+One&family=Raleway:wght@400;700&display=swap" rel="stylesheet">
<style>
  :root {
    --backdrop: #5f5f5f;
    --paper: #f4f6f0;
    --leaf-green: #7cb342;
    --ink: #555555;
    --white: #ffffff;
    --sign-red: #e3262b;
    --sign-black: #111111;
  }
  * { margin: 0; padding: 0; box-sizing: border-box; }
  html, body {
    width: 686px; height: 1200px; overflow: hidden;
    background: var(--backdrop);
  }
  .menu-card {
    position: absolute; left: 134px; top: 100px;
    width: 418px; height: 998px;
    background: var(--paper);
    overflow: hidden;
  }
  .leaf-texture {
    position: absolute; inset: 0;
    background: linear-gradient(180deg, #f1f4ec 0%, #f6f7f2 50%, #f1f4ec 100%);
  }
  .title-band {
    position: absolute; left: 0; top: 60px; width: 100%; height: 200px;
    background: var(--leaf-green);
  }
  .title {
    position: absolute; left: 0; top: 84px; width: 100%;
    text-align: center;
    font-family: "Germania One", serif;
    font-size: 118px; line-height: 1;
    color: var(--white); letter-spacing: 2px;
  }
  .section-head {
    position: absolute; left: 66px; width: 306px;
    border-bottom: 2px solid var(--leaf-green);
    height: 60px;
  }
  .section-head.weed { top: 290px; }
  .section-head.hash { top: 646px; }
  .section-title {
    position: absolute; left: 0; bottom: 6px;
    display: flex; align-items: center; gap: 4px;
    font-family: "Germania One", serif;
    font-size: 54px; line-height: 1;
    color: var(--leaf-green); letter-spacing: 1px;
  }
  .leaf-icon { width: 30px; height: 30px; flex: none; }
  .unit {
    position: absolute; right: 12px; bottom: 14px;
    font-family: "Raleway", sans-serif; font-weight: 700;
    font-size: 17px; color: var(--leaf-green);
  }
  .price-list {
    position: absolute; left: 66px; width: 306px; list-style: none;
  }
  .price-list.weed { top: 381px; }
  .price-list.hash { top: 733px; }
  .price-list li {
    display: flex; justify-content: space-between;
    height: 38.5px; line-height: 38.5px;
    font-family: "Germania One", serif; font-size: 35px;
    color: var(--ink);
  }
  .price { width: 64px; text-align: left; letter-spacing: 2px; }
  .price .euro { font-family: "Raleway", sans-serif; font-weight: 400; font-size: 24px; letter-spacing: 0; }
  .no-smoking {
    position: absolute; left: 76px; top: 920px;
    display: flex; align-items: center; gap: 14px;
    font-family: "Raleway", sans-serif; font-weight: 700;
    font-size: 25px; color: var(--ink);
  }
</style>
</head>
<body>
  <svg width="0" height="0" style="position:absolute" aria-hidden="true">
    <defs>
      <symbol id="cannabis-leaf" viewBox="0 0 40 40">
        <g fill="currentColor">
          <ellipse cx="20" cy="12" rx="3" ry="12"/>
          <ellipse cx="20" cy="12" rx="2.6" ry="10" transform="rotate(-35 20 24)"/>
          <ellipse cx="20" cy="12" rx="2.6" ry="10" transform="rotate(35 20 24)"/>
          <ellipse cx="20" cy="14" rx="2.2" ry="8" transform="rotate(-75 20 24)"/>
          <ellipse cx="20" cy="14" rx="2.2" ry="8" transform="rotate(75 20 24)"/>
          <rect x="19.2" y="24" width="1.6" height="12"/>
        </g>
      </symbol>
    </defs>
  </svg>

  <main class="menu-card">
    <div class="leaf-texture" role="img" aria-label="Faint pattern of cannabis leaves across the card"></div>
    <div class="title-band" role="img" aria-label="Green band with a fringe of cannabis leaves along its top and bottom edges"></div>
    <h1 class="title">MENU</h1>

    <div class="section-head weed">
      <h2 class="section-title">WEED<svg class="leaf-icon" aria-hidden="true"><use href="#cannabis-leaf"/></svg></h2>
      <span class="unit">P/G</span>
    </div>
    <ul class="price-list weed">
      <li><span>Vortigan</span><span class="price"><span class="euro">€</span>16</span></li>
      <li><span>Tangerosa</span><span class="price"><span class="euro">€</span>14</span></li>
      <li><span>Dusk Rover</span><span class="price"><span class="euro">€</span>14</span></li>
      <li><span>Mangolina</span><span class="price"><span class="euro">€</span>16</span></li>
      <li><span>Ultra Fern</span><span class="price"><span class="euro">€</span>14</span></li>
      <li><span>Amber Hermit</span><span class="price"><span class="euro">€</span>14</span></li>
    </ul>

    <div class="section-head hash">
      <h2 class="section-title">HASH<svg class="leaf-icon" aria-hidden="true"><use href="#cannabis-leaf"/></svg></h2>
      <span class="unit">P/G</span>
    </div>
    <ul class="price-list hash">
      <li><span>Nepali Bronze</span><span class="price"><span class="euro">€</span>12</span></li>
      <li><span>Velvet Ember</span><span class="price"><span class="euro">€</span>11</span></li>
      <li><span>Cedar Pine</span><span class="price"><span class="euro">€</span>14</span></li>
      <li><span>Red Fable</span><span class="price"><span class="euro">€</span>10</span></li>
    </ul>

    <div class="no-smoking">
      <svg width="58" height="58" viewBox="0 0 58 58" aria-hidden="true">
        <circle cx="29" cy="29" r="26" fill="var(--white)" stroke="var(--sign-red)" stroke-width="5"/>
        <rect x="12" y="31" width="28" height="7" fill="var(--sign-black)"/>
        <rect x="40" y="31" width="4" height="7" fill="var(--sign-black)"/>
        <path d="M38 27 q-4 -5 0 -9 q4 -4 0 -8" fill="none" stroke="var(--sign-black)" stroke-width="2"/>
        <line x1="11" y1="11" x2="47" y2="47" stroke="var(--sign-red)" stroke-width="5"/>
      </svg>
      <span>No Cigarettes</span>
    </div>
  </main>
</body>
</html>
```